Carpentry Fitouts business Van half wrap

We are looking for a half wrap on our 2020Mitsubishi Express van.
Template attached, base colour to be white

Van colour is white. The 2 blue colours from logo plus black should be used in the half wrap

Our services are :
Commercial Carpentry
Interior Fitouts
Plastering
Suspended Ceilings
Windows & Doors

Rear window to have perforated one way film

Contact details on van should be PH:0491 582 306
liam@quillmarkfitouts.com.au

Industry/Entity Type

Carpentry Fitouts

Colors
0054AA
0677BA
7BADD7
CADEEF
E8F1F8
0094D4
00A9DD
6FCCEA
C7EBF8
E9F6FB

Requirements
Nice to have
• Wrap not through door handles

```html
<!DOCTYPE html>
<html lang="en">
<head>
<meta charset="utf-8">
<title>Quillmark Fitouts – Van Half Wrap</title>
<link rel="stylesheet" href="https://fonts.googleapis.com/css2?family=Oswald:wght@300&family=Roboto+Condensed:wght@700&display=swap">
<style>
  :root {
    --navy: #1f2a6e;
    --cyan: #1a9fc6;
    --black: #1c1c1e;
    --panel-white: #ffffff;
    --glass: #c9cdd3;
    --hub: #9a9ea4;
    --lamp: #b3262b;
    --line: #2a2a2a;
  }
  html, body { margin: 0; padding: 0; overflow: hidden; }
  body { width: 1200px; height: 1200px; background: #ffffff; position: relative; }
  .view { position: absolute; display: block; }
  .side-view { left: 30px; top: 50px; width: 1140px; height: 500px; }
  .rear-view { left: 40px; top: 600px; width: 520px; height: 560px; }
  .front-view { left: 590px; top: 600px; width: 570px; height: 560px; }
  .brand-name { font-family: "Oswald", sans-serif; font-weight: 300; fill: var(--panel-white); }
  .brand-name.on-white { fill: var(--navy); }
  .contact { font-family: "Roboto Condensed", sans-serif; font-weight: 700; fill: var(--panel-white); }
  .contact.on-white { fill: var(--navy); }
  .service-list { font-family: "Roboto Condensed", sans-serif; font-weight: 700; }
  .service-list.navy { fill: var(--navy); }
  .service-list.white { fill: var(--panel-white); }
</style>
</head>
<body>

<!-- Side elevation -->
<svg class="view side-view" viewBox="0 0 1140 500" aria-label="Side elevation of the half wrap">
  <path d="M40,60 Q40,30 75,30 L930,30 Q980,30 1010,70 L1100,200 Q1120,225 1120,270 L1120,430 L40,430 Z" fill="var(--panel-white)" stroke="var(--line)" stroke-width="2"/>
  <path d="M40,60 Q40,30 75,30 L590,30 L560,60 L500,380 L300,380 L300,430 L40,430 Z" fill="var(--navy)"/>
  <circle cx="445" cy="225" r="195" fill="var(--navy)"/>
  <rect x="40" y="10" width="3" height="1" fill="none"/>
  <text class="brand-name" x="70" y="135" font-size="58" textLength="400" lengthAdjust="spacingAndGlyphs">QUILLMARK FITOUTS</text>
  <rect x="40" y="178" width="420" height="6" fill="var(--panel-white)"/>
  <rect x="40" y="184" width="420" height="40" fill="var(--cyan)"/>
  <text class="contact" x="60" y="213" font-size="20">liam@quillmarkfitouts.com.au</text>
  <rect x="40" y="240" width="420" height="44" fill="var(--cyan)"/>
  <rect x="40" y="284" width="420" height="6" fill="var(--panel-white)"/>
  <text class="contact" x="60" y="277" font-size="38">0491 582 306</text>
  <path d="M650,50 L860,50 Q900,50 920,80 L960,160 L960,210 L650,190 Z" fill="var(--glass)" stroke="var(--line)" stroke-width="2"/>
  <line x1="635" y1="40" x2="635" y2="400" stroke="var(--line)" stroke-width="2"/>
  <line x1="915" y1="40" x2="915" y2="400" stroke="var(--line)" stroke-width="2"/>
  <rect x="580" y="252" width="60" height="9" rx="4" fill="var(--black)"/>
  <g class="service-list navy" font-size="19">
    <text x="700" y="262">• Commercial Carpentry</text>
    <text x="700" y="288">• Interior Fitouts</text>
    <text x="700" y="314">• Plastering</text>
    <text x="700" y="340">• Suspended Ceilings</text>
    <text x="700" y="366">• Windows &amp; Doors</text>
  </g>
  <path d="M1060,300 L1120,300 L1120,430 L1000,430 Z" fill="var(--black)"/>
  <rect x="300" y="390" width="700" height="40" fill="var(--black)"/>
  <circle cx="210" cy="420" r="72" fill="var(--black)"/>
  <circle cx="210" cy="420" r="42" fill="var(--hub)"/>
  <circle cx="930" cy="420" r="72" fill="var(--black)"/>
  <circle cx="930" cy="420" r="42" fill="var(--hub)"/>
</svg>

<!-- Rear elevation -->
<svg class="view rear-view" viewBox="0 0 520 560" aria-label="Rear elevation of the half wrap">
  <rect x="10" y="10" width="500" height="520" rx="20" fill="var(--black)"/>
  <rect x="50" y="10" width="420" height="470" rx="10" fill="var(--navy)"/>
  <rect x="50" y="250" width="420" height="6" fill="var(--panel-white)"/>
  <rect x="50" y="256" width="420" height="120" fill="var(--cyan)"/>
  <rect x="50" y="376" width="420" height="6" fill="var(--panel-white)"/>
  <circle cx="145" cy="250" r="95" fill="var(--navy)"/>
  <line x1="260" y1="10" x2="260" y2="480" stroke="#151a45" stroke-width="2"/>
  <g class="service-list white" font-size="14">
    <text x="275" y="60">• Commercial Carpentry</text>
    <text x="275" y="80">• Interior Fitouts</text>
    <text x="275" y="100">• Plastering</text>
    <text x="275" y="120">• Suspended Ceilings</text>
    <text x="275" y="140">• Windows &amp; Doors</text>
  </g>
  <text class="brand-name" x="250" y="350" font-size="56" textLength="210" lengthAdjust="spacingAndGlyphs">QUILLMARK FITOUTS</text>
  <text class="contact" x="65" y="420" font-size="15">liam@quillmarkfitouts.com.au</text>
  <text class="contact" x="275" y="425" font-size="27">0491 582 306</text>
  <rect x="20" y="150" width="26" height="110" rx="6" fill="var(--lamp)"/>
  <rect x="474" y="150" width="26" height="110" rx="6" fill="var(--lamp)"/>
  <rect x="190" y="14" width="60" height="14" rx="3" fill="var(--lamp)"/>
</svg>

<!-- Front elevation -->
<svg class="view front-view" viewBox="0 0 570 560" aria-label="Front elevation of the half wrap">
  <path d="M80,30 L490,30 L520,200 L540,300 L540,520 L30,520 L30,300 L50,200 Z" fill="var(--panel-white)" stroke="var(--line)" stroke-width="2"/>
  <path d="M95,40 L475,40 L500,185 L70,185 Z" fill="var(--glass)"/>
  <path d="M30,320 L540,320 L540,520 L30,520 Z" fill="var(--black)"/>
  <circle cx="150" cy="258" r="34" fill="var(--navy)"/>
  <text class="brand-name on-white" x="195" y="278" font-size="40" textLength="245" lengthAdjust="spacingAndGlyphs">QUILLMARK FITOUTS</text>
  <text class="contact on-white" x="205" y="300" font-size="12">liam@quillmarkfitouts.com.au</text>
  <rect x="5" y="160" width="40" height="55" rx="8" fill="var(--black)"/>
  <rect x="525" y="160" width="40" height="55" rx="8" fill="var(--black)"/>
</svg>

</body>
</html>
```